チラシに使用する文章と画像はこちらで用意いたします。
全体の雰囲気はimageBのような感じです。
作りたいチラシのイメージはimageAのとおりです。
デザインは自由に調整いただいてかまいません。
使用する色はimageBのような「黒、茶」を考えておりますが、自由に調整いただいて結構です。

使用する文章はPDFファイルを参照下さい。
imageAのAからIはPDFの文章を入れて下さい。

imageAのDにいれる画像は「health.zip」をご使用下さい。
imageAのEにいれる画像は「urinary organs.zip」をご使用下さい。
imageAのFにいれる画像は「digestive organs.zip」をご使用下さい。
画像はimageBのように並べて下さい。

またimageAのD、E、Fのハーブの画像の上に「ORU・PLANTIVA」のマークを入れて下さい。
詳しくはimageAをご参照ください。
マークの画像はimageCをお使い下さい。
有機農作物はマークがないため、有機農作物と記載して下さい。
A4
片面
黒 茶色
• 高解像度JPG (.jpg)
• イラストレーター形式 (.ai)

柔らかい雰囲気やデザインなどとても気に入りました。
色合いも落ち着いているので、読みやすかったです。

たくさん提案くださり、誠にありがとうございます。
また機会があれば、どうぞよろしくお願い致します。

```html
<!DOCTYPE html>
<html lang="ja">
<head>
<meta charset="utf-8">
<title>大切な家族だから ハーブのご案内</title>
<link rel="stylesheet" href="https://fonts.googleapis.com/css2?family=Shippori+Mincho:wght@600;800&family=Noto+Sans+JP:wght@400;700&display=swap">
<style>
:root{
  --ink:#2b1a10;
  --brown:#6b3f1f;
  --brown-soft:#a77a52;
  --cream:#f6efe4;
  --paper:#ffffff;
  --rule:#c9a983;
}
*{box-sizing:border-box;margin:0;padding:0}
html,body{width:849px;height:1200px;overflow:hidden;background:var(--paper)}
.flyer{position:relative;width:849px;height:1200px;font-family:"Noto Sans JP",sans-serif;color:var(--ink);overflow:hidden}
.abs{position:absolute}
.photo{border-radius:6px}
.headline{left:140px;width:569px;top:10px;text-align:center;font-family:"Shippori Mincho",serif;color:var(--brown);font-weight:800;line-height:1.15}
.headline .l1{font-size:30px;display:block}
.headline .l2{font-size:31px;display:block}
.headline .sub{display:block;margin-top:8px;font-size:20px;color:var(--ink);font-weight:600}
.para{left:34px;width:781px;font-size:11px;line-height:1.65}
.subhead{left:34px;width:781px;text-align:center;font-family:"Shippori Mincho",serif;font-weight:800;font-size:18px;color:var(--brown);border-bottom:1px solid var(--rule);padding-bottom:2px}
.bar{left:34px;width:781px;height:26px;display:flex;align-items:center;gap:8px;padding:0 10px;background:var(--cream);border-left:6px solid var(--brown);font-weight:700;font-size:15px;color:var(--brown)}
.bar .price{margin-left:6px}
.bar .mark{margin-left:auto;display:flex;align-items:center;gap:5px;font-size:11px;font-weight:700;color:var(--brown)}
.bar .mark i{display:block;width:10px;height:10px;background:var(--brown)}
.row{display:flex;gap:9px}
.herb{display:flex;flex-direction:column;align-items:center}
.herb .swatch{width:100%;border-radius:3px}
.herb figcaption{font-size:9px;margin-top:3px;white-space:nowrap}
.heading-plain{font-family:"Shippori Mincho",serif;font-weight:800;font-size:18px;color:var(--brown)}
.band{left:34px;width:781px;height:28px;background:var(--brown);color:#fff;font-weight:700;font-size:15px;display:flex;align-items:center;justify-content:center;letter-spacing:.2em}
.footer{left:34px;width:781px;font-size:10.5px;line-height:1.6}
.g1{background:linear-gradient(135deg,#8a9a5b,#c8c29a)}
.g2{background:linear-gradient(135deg,#c9b27a,#eee2b8)}
.g3{background:linear-gradient(135deg,#6f7d45,#a8a878)}
.g4{background:linear-gradient(135deg,#a2764a,#d8c09a)}
.g5{background:linear-gradient(135deg,#b79b6a,#e7dcc0)}
</style>
</head>
<body>
<main class="flyer">

  <div class="abs photo" style="left:10px;top:10px;width:120px;height:112px;background:linear-gradient(160deg,#e2a55a,#f3dfb5)" role="img" aria-label="子猫と子犬の写真"></div>
  <div class="abs photo" style="left:719px;top:10px;width:120px;height:112px;background:linear-gradient(160deg,#eceae4,#9cae7a)" role="img" aria-label="白い子犬たちの写真"></div>

  <h1 class="abs headline">
    <span class="l1">大切な家族だから</span>
    <span class="l2">いつまでも若々しく元気にいてほしい</span>
    <span class="sub">現代の犬、猫にこそハーブをおすすめします</span>
  </h1>

  <p class="abs para" style="top:130px">現代の犬や猫は、食生活や住環境の変化により、体に負担を抱えやすくなっています。毎日の食事にハーブを少し加えることで、体の内側から健やかさを支えることができます。ハーブは古くから人と動物の暮らしに寄り添ってきた植物です。自然の力を取り入れ、大切な家族が元気に過ごせるようお手伝いします。毎日のごはんに少量ずつ混ぜてお使いください。</p>

  <h2 class="abs subhead" style="top:186px">特筆すべきは抗酸化作用</h2>
  <p class="abs para" style="top:214px">ハーブには植物が自らを守るために作り出す成分が多く含まれ、体の酸化を防ぐ働きが期待されます。年齢とともに気になる衰えをやさしくケアし、若々しさを保つ助けになります。</p>

  <h2 class="abs subhead" style="top:258px">腸内環境を整える</h2>
  <p class="abs para" style="top:286px">ハーブに含まれる食物繊維や香りの成分は、おなかの調子を整えるのに役立ちます。腸内環境が整うと、毛づやや体調の変化にも良い影響が期待できます。</p>

  <!-- Section 1 -->
  <div class="abs bar" style="top:330px"><span>健康増進用ハーブ</span><span class="price">25g入り　1260円</span><span class="mark"><i></i>ORU・PLANTIVA</span></div>
  <div class="abs photo" style="left:34px;top:364px;width:150px;height:100px;background:linear-gradient(150deg,#c99a5e,#9b8a55)" role="img" aria-label="草の上でくつろぐ犬の写真"></div>
  <div class="abs row" style="left:196px;top:364px">
    <figure class="herb" style="width:96px"><div class="swatch g1" style="height:70px" role="img" aria-label="ハーブの写真"></div><figcaption>カモミール</figcaption></figure>
    <figure class="herb" style="width:96px"><div class="swatch g3" style="height:70px" role="img" aria-label="ハーブの写真"></div><figcaption>ネトル</figcaption></figure>
    <figure class="herb" style="width:96px"><div class="swatch g2" style="height:70px" role="img" aria-label="ハーブの写真"></div><figcaption>ローズヒップ</figcaption></figure>
    <figure class="herb" style="width:96px"><div class="swatch g1" style="height:70px" role="img" aria-label="ハーブの写真"></div><figcaption>ペパーミント</figcaption></figure>
    <figure class="herb" style="width:96px"><div class="swatch g4" style="height:70px" role="img" aria-label="ハーブの写真"></div><figcaption>フェンネル</figcaption></figure>
    <figure class="herb" style="width:96px"><div class="swatch g5" style="height:70px" role="img" aria-label="ハーブの写真"></div><figcaption>アルファルファ</figcaption></figure>
  </div>
  <div class="abs row" style="left:34px;top:474px">
    <figure class="herb" style="width:104px"><div class="swatch g3" style="height:60px" role="img" aria-label="ハーブの写真"></div><figcaption>パセリ</figcaption></figure>
    <figure class="herb" style="width:104px"><div class="swatch g1" style="height:60px" role="img" aria-label="ハーブの写真"></div><figcaption>セージ</figcaption></figure>
    <figure class="herb" style="width:104px"><div class="swatch g4" style="height:60px" role="img" aria-label="ハーブの写真"></div><figcaption>ダンデライオン</figcaption></figure>
    <figure class="herb" style="width:104px"><div class="swatch g2" style="height:60px" role="img" aria-label="ハーブの写真"></div><figcaption>レモンバーム</figcaption></figure>
    <figure class="herb" style="width:104px"><div class="swatch g3" style="height:60px" role="img" aria-label="ハーブの写真"></div><figcaption>タイム</figcaption></figure>
    <figure class="herb" style="width:104px"><div class="swatch g5" style="height:60px" role="img" aria-label="ハーブの写真"></div><figcaption>ジンジャー</figcaption></figure>
    <figure class="herb" style="width:104px"><div class="swatch g1" style="height:60px" role="img" aria-label="ハーブの写真"></div><figcaption>ローズマリー</figcaption></figure>
  </div>
  <p class="abs para" style="top:560px">毎日の健康維持に役立つハーブをバランスよく配合しました。食欲や元気が気になる子に、いつものごはんへ少量ずつ加えてお使いください。</p>

  <!-- Section 2 -->
  <div class="abs bar" style="top:604px"><span>泌尿器系応援ハーブ</span><span class="price">25g入り　1260円</span><span class="mark"><i></i>ORU・PLANTIVA</span></div>
  <div class="abs photo" style="left:34px;top:638px;width:150px;height:100px;background:linear-gradient(150deg,#b58b5a,#7d8a4e)" role="img" aria-label="芝生に座る犬の写真"></div>
  <div class="abs row" style="left:196px;top:638px">
    <figure class="herb" style="width:96px"><div class="swatch g4" style="height:70px" role="img" aria-label="ハーブの写真"></div><figcaption>クランベリー</figcaption></figure>
    <figure class="herb" style="width:96px"><div class="swatch g1" style="height:70px" role="img" aria-label="ハーブの写真"></div><figcaption>ホーステール</figcaption></figure>
    <figure class="herb" style="width:96px"><div class="swatch g3" style="height:70px" role="img" aria-label="ハーブの写真"></div><figcaption>ネトル</figcaption></figure>
    <figure class="herb" style="width:96px"><div class="swatch g5" style="height:70px" role="img" aria-label="ハーブの写真"></div><figcaption>コーンシルク</figcaption></figure>
    <figure class="herb" style="width:96px"><div class="swatch g2" style="height:70px" role="img" aria-label="ハーブの写真"></div><figcaption>マシュマロウ</figcaption></figure>
    <figure class="herb" style="width:96px"><div class="swatch g1" style="height:70px" role="img" aria-label="ハーブの写真"></div><figcaption>パセリ</figcaption></figure>
  </div>
  <p class="abs para" style="top:744px">年齢とともに気になりやすい尿のトラブルに。水分と一緒に摂りやすく、体の巡りをやさしくサポートするハーブを集めました。</p>

  <!-- Section 3 -->
  <div class="abs bar" style="top:784px"><span>消化器系応援ハーブ</span><span class="price">25g入り　1260円</span><span class="mark"><i></i>ORU・PLANTIVA</span></div>
  <div class="abs row" style="left:34px;top:818px">
    <figure class="herb" style="width:104px"><div class="swatch g1" style="height:60px" role="img" aria-label="ハーブの写真"></div><figcaption>ペパーミント</figcaption></figure>
    <figure class="herb" style="width:104px"><div class="swatch g5" style="height:60px" role="img" aria-label="ハーブの写真"></div><figcaption>スリッパリーエルム</figcaption></figure>
    <figure class="herb" style="width:104px"><div class="swatch g4" style="height:60px" role="img" aria-label="ハーブの写真"></div><figcaption>フェンネル</figcaption></figure>
    <figure class="herb" style="width:104px"><div class="swatch g2" style="height:60px" role="img" aria-label="ハーブの写真"></div><figcaption>カモミール</figcaption></figure>
    <figure class="herb" style="width:104px"><div class="swatch g3" style="height:60px" role="img" aria-label="ハーブの写真"></div><figcaption>レモンバーム</figcaption></figure>
    <figure class="herb" style="width:104px"><div class="swatch g5" style="height:60px" role="img" aria-label="ハーブの写真"></div><figcaption>ジンジャー</figcaption></figure>
    <figure class="herb" style="width:104px"><div class="swatch g1" style="height:60px" role="img" aria-label="ハーブの写真"></div><figcaption>ディル</figcaption></figure>
  </div>
  <p class="abs para" style="top:902px">おなかがデリケートな子、便の調子が気になる子に。胃腸にやさしいハーブで、毎日のすっきりを応援します。</p>

  <!-- Organic -->
  <div class="abs photo" style="left:34px;top:944px;width:150px;height:110px;background:linear-gradient(150deg,#8c7a63,#cbb79a)" role="img" aria-label="くつろぐ猫の写真"></div>
  <h3 class="abs heading-plain" style="left:196px;top:942px">有機ハーブ</h3>
  <div class="abs row" style="left:196px;top:972px">
    <figure class="herb" style="width:116px"><div class="swatch g3" style="height:54px" role="img" aria-label="有機ハーブの写真"></div><figcaption>有機カモミール</figcaption></figure>
    <figure class="herb" style="width:116px"><div class="swatch g2" style="height:54px" role="img" aria-label="有機ハーブの写真"></div><figcaption>有機ネトル</figcaption></figure>
    <figure class="herb" style="width:116px"><div class="swatch g1" style="height:54px" role="img" aria-label="有機ハーブの写真"></div><figcaption>有機ミント</figcaption></figure>
    <figure class="herb" style="width:116px"><div class="swatch g4" style="height:54px" role="img" aria-label="有機ハーブの写真"></div><figcaption>有機ローズ</figcaption></figure>
    <figure class="herb" style="width:116px"><div class="swatch g5" style="height:54px" role="img" aria-label="有機ハーブの写真"></div><figcaption>有機セージ</figcaption></figure>
  </div>
  <h3 class="abs heading-plain" style="left:34px;top:1064px">農薬不使用ハーブ</h3>
  <p class="abs para" style="left:210px;width:605px;top:1068px">栽培期間中、農薬を使わずに育てたハーブです。香りと風味をそのままお届けします。</p>

  <div class="abs band" style="top:1106px">有機農産物</div>
  <p class="abs footer" style="top:1144px">有機農産物とは、化学合成された農薬や肥料を使わずに栽培された農作物です。原料はすべて信頼できる産地から選び、ひとつひとつ丁寧に仕上げています。大切な家族の毎日に、安心してお使いいただけます。</p>

</main>
</body>
</html>
```